Talvo shoes is a wholesale shoe sales company , mostly working in female shoes and kiddies shoes with a small mens section . looking for a clean slick look. http://www.kemrafootwear.co.za/shop/ is a good reference

It Company

```html
<!DOCTYPE html>
<html lang="en">
<head>
<meta charset="utf-8">
<title>Talvo shoes</title>
<link href="https://fonts.googleapis.com/css2?family=Mulish:wght@300;400;600;700&display=swap" rel="stylesheet">
<style>
:root{
  --bg:#000;
  --panel:#151515;
  --band:#0b0b0b;
  --accent:#f39a1e;
  --text:#d9d9d9;
  --muted:#9a9a9a;
  --line:#2e2e2e;
  --white:#fff;
}
*{margin:0;padding:0;box-sizing:border-box}
html,body{width:837px;height:1200px;overflow:hidden;background:var(--bg)}
body{font-family:"Mulish",Arial,sans-serif;color:var(--text);position:relative}
.abs{position:absolute}

/* header */
.brand{left:113px;top:22px;font-size:38px;font-weight:600;color:var(--accent);letter-spacing:.5px}
.flags{left:607px;top:14px;display:flex;gap:6px}
.flag{width:19px;height:13px;display:block}
.account-bar{left:447px;top:40px;width:280px;height:13px;background:linear-gradient(90deg,rgba(60,60,60,0),#3a3a3a 35%,#444);display:flex;justify-content:flex-end;gap:18px;padding-right:6px;font-size:7.5px;line-height:13px;color:#bdbdbd}
.main-nav{top:104px;left:0;width:837px;font-size:13px}
.main-nav a{position:absolute;color:var(--muted);text-decoration:none;white-space:nowrap}
.main-nav a.active{color:var(--accent)}
.header-rule{left:0;top:133px;width:837px;height:2px;background:linear-gradient(90deg,#111,#3a3a3a 50%,#111)}

/* hero */
.hero{left:0;top:135px;width:837px;height:340px;background:radial-gradient(ellipse at 50% 40%,#2c2c2c 0%,#141414 55%,#000 100%)}
.hero-band{left:113px;top:267px;width:614px;height:53px;background:linear-gradient(90deg,rgba(0,0,0,0),#050505 20%,#050505 80%,rgba(0,0,0,0))}
.hero-title{left:113px;top:168px;width:100px;font-size:22px;font-weight:300;line-height:30px;color:var(--accent);text-align:right}
.hero-title span{display:block}
.hero-title span:first-child{text-align:left}
.hero-photo{left:292px;top:177px;width:253px;height:214px;background:linear-gradient(160deg,#c9a27c,#8a5a3a 45%,#d8b07a 75%,#6f4a30)}
.hero-arrow{top:281px;width:18px;height:24px}
.dots{left:355px;top:445px;display:flex;gap:13px}
.dot{width:7px;height:4px;border-radius:2px;background:#555}
.dot.on{background:var(--accent)}

/* thumbnails */
.strip{left:0;top:477px;width:837px;height:120px;background:linear-gradient(180deg,#1a1a1a,#2a2a2a 50%,#0e0e0e);border-top:1px solid #333;border-bottom:1px solid #333}
.thumb-cell{top:483px;width:1px;height:110px;background:#444}
.thumb{top:499px;width:120px;height:78px}
.thumb.light{background:linear-gradient(135deg,#fafafa,#e9dcc8 50%,#f2f2f2)}
.thumb.dark{background:linear-gradient(135deg,#f7f7f7,#3a3a3a 50%,#f3f3f3)}
.thumb.scene{background:linear-gradient(160deg,#c9a27c,#8a5a3a 50%,#d8b07a)}
.strip-arrow{top:505px;width:12px;height:62px}

/* content */
.col-heading{font-size:17px;font-weight:400;color:var(--white)}
.col-text{font-size:9.8px;line-height:12.9px;letter-spacing:-.1px;color:var(--text);width:172px;hyphens:auto;-webkit-hyphens:auto}
.col-text p+p{margin-top:13px}
.divider{left:307px;top:655px;width:1px;height:278px;background:linear-gradient(180deg,#333,#555,#222)}
.news-item{left:344px;width:383px;font-size:12px;line-height:14px}
.news-date{position:absolute;left:0;top:0;color:var(--white)}
.news-body{margin-left:73px}
.news-title{color:var(--accent);font-weight:700}
.news-text{color:var(--text);text-align:justify}
.news-photo{left:419px;top:727px;width:306px;height:236px;background:linear-gradient(170deg,#caa08a,#b88a73 40%,#6d5238 65%,#b57a64)}
.more-arrow{left:655px;top:1104px;width:72px;height:10px}

/* footer */
.footer-rule{left:0;top:1124px;width:837px;height:1px;background:linear-gradient(90deg,#000,#333 50%,#000)}
.footer-nav{top:1140px;left:0;width:837px;font-size:12px}
.footer-nav a{position:absolute;color:#777;text-decoration:none;white-space:nowrap}
.footer-nav a.active{color:var(--accent)}
.copyright{left:0;top:1167px;width:837px;text-align:center;font-size:9px;color:var(--white)}
</style>
</head>
<body>

<header>
  <div class="abs brand">Talvo shoes</div>

  <div class="abs flags" aria-label="Languages">
    <svg class="flag" viewBox="0 0 19 13" aria-label="English"><rect width="19" height="13" fill="#012169"/><path d="M0 0L19 13M19 0L0 13" stroke="#fff" stroke-width="3"/><path d="M0 0L19 13M19 0L0 13" stroke="#c8102e" stroke-width="1"/><path d="M9.5 0V13M0 6.5H19" stroke="#fff" stroke-width="4"/><path d="M9.5 0V13M0 6.5H19" stroke="#c8102e" stroke-width="2"/></svg>
    <svg class="flag" viewBox="0 0 3 2" aria-label="French"><rect width="1" height="2" fill="#0055a4"/><rect x="1" width="1" height="2" fill="#fff"/><rect x="2" width="1" height="2" fill="#ef4135"/></svg>
    <svg class="flag" viewBox="0 0 3 3" preserveAspectRatio="none" aria-label="German"><rect width="3" height="1" fill="#000"/><rect y="1" width="3" height="1" fill="#dd0000"/><rect y="2" width="3" height="1" fill="#ffce00"/></svg>
    <svg class="flag" viewBox="0 0 3 3" preserveAspectRatio="none" aria-label="Dutch"><rect width="3" height="1" fill="#ae1c28"/><rect y="1" width="3" height="1" fill="#fff"/><rect y="2" width="3" height="1" fill="#21468b"/></svg>
    <svg class="flag" viewBox="0 0 3 2" preserveAspectRatio="none" aria-label="Belgian"><rect width="1" height="2" fill="#000"/><rect x="1" width="1" height="2" fill="#fdda24"/><rect x="2" width="1" height="2" fill="#ef3340"/></svg>
  </div>

  <div class="abs account-bar">
    <span>My Account</span><span>My Orders</span><span>My Address</span>
  </div>

  <nav class="abs main-nav">
    <a class="active" style="left:337px">Home</a>
    <a style="left:393px">About Us</a>
    <a style="left:463px">Talvo Store</a>
    <a style="left:543px">Talvo Events</a>
    <a style="left:631px">News</a>
    <a style="left:684px">Contact</a>
  </nav>
  <div class="abs header-rule"></div>
</header>

<section class="hero-section">
  <div class="abs hero"></div>
  <div class="abs hero-band"></div>
  <h1 class="abs hero-title"><span>WOMAN</span><span>SHOES</span></h1>
  <div class="abs hero-photo" role="img" aria-label="Photo of a woman's legs walking in strappy high-heeled sandals"></div>
  <svg class="abs hero-arrow" style="left:254px" viewBox="0 0 18 24"><path d="M15 4L3 12L15 20" fill="none" stroke="#777" stroke-width="1.5"/></svg>
  <svg class="abs hero-arrow" style="left:566px" viewBox="0 0 18 24"><path d="M3 4L15 12L3 20" fill="none" stroke="#777" stroke-width="1.5"/></svg>
  <div class="abs dots"><i class="dot"></i><i class="dot"></i><i class="dot on"></i><i class="dot"></i><i class="dot"></i><i class="dot"></i><i class="dot"></i></div>
</section>

<section class="thumb-strip">
  <div class="abs strip"></div>
  <svg class="abs strip-arrow" style="left:10px" viewBox="0 0 12 62"><path d="M10 2L2 31L10 60" fill="none" stroke="#888" stroke-width="1.5"/></svg>
  <svg class="abs strip-arrow" style="left:814px" viewBox="0 0 12 62"><path d="M2 2L10 31L2 60" fill="none" stroke="#888" stroke-width="1.5"/></svg>
  <div class="abs thumb-cell" style="left:188px"></div>
  <div class="abs thumb-cell" style="left:341px"></div>
  <div class="abs thumb-cell" style="left:494px"></div>
  <div class="abs thumb-cell" style="left:648px"></div>
  <div class="abs thumb light" style="left:52px" role="img" aria-label="Cream and coral peep-toe high heel"></div>
  <div class="abs thumb dark" style="left:205px" role="img" aria-label="Pair of black patent high heels"></div>
  <div class="abs thumb scene" style="left:357px" role="img" aria-label="Legs walking in strappy sandals"></div>
  <div class="abs thumb dark" style="left:511px" role="img" aria-label="Pair of black patent high heels"></div>
  <div class="abs thumb light" style="left:664px" role="img" aria-label="Cream and coral peep-toe high heel"></div>
</section>

<main>
  <h2 class="abs col-heading" style="left:113px;top:648px">Who we are?</h2>
  <div class="abs col-text" style="left:113px;top:674px">
    <p>Lorem ipsum dolor sit amet, consectetuer adipiscing elit. Aenean commodo ligula eget dolor. Aenean massa. Cum sociis natoque penatibus et magnis dis parturient montes, nascetur ridiculus mus.</p>
    <p>Nullam dictum felis eu pede mollis pretium. Integer tincidunt. Cras dapibus. Vivamus elementum semper nisi. Aenean vulputate eleifend tellus. Aenean leo ligula, porttitor eu, consequat vitae, eleifend ac, enim. Aliquam lorem ante, dapibus in, viverra quis, feugiat a, tellus.</p>
    <p>Phasellus viverra nulla ut metus varius laoreet. Quisque rutrum. Aenean imperdiet. Etiam ultricies nisi vel augue. Curabitur ullamcorper ultricies nisi. Nam eget dui. Etiam rhoncus.</p>
  </div>

  <h2 class="abs col-heading" style="left:113px;top:980px">What we do?</h2>
  <div class="abs col-text" style="left:113px;top:1006px">
    <p>Donec quam felis, ultricies nec, pellentesque eu, pretium quis, sem. Nulla consequat massa quis enim. Donec pede justo, fringilla vel, aliquet nec, vulputate eget, arcu. In enim justo, rhoncus ut, imperdiet a, venenatis vitae, justo.</p>
  </div>

  <div class="abs divider"></div>

  <h2 class="abs col-heading" style="left:344px;top:648px">Latest News</h2>

  <article class="abs news-item" style="top:678px">
    <span class="news-date">(5/18/2014)</span>
    <div class="news-body">
      <div class="news-title">Lorem ipsum dolor sit amet</div>
      <div class="news-text">Lorem ipsum dolor sit amet, consectetuer adipiscing elit. Aenean commodo ligula eget dolor. Aenean massa.</div>
    </div>
  </article>
  <div class="abs news-photo" role="img" aria-label="Woman in a white dress seated on a green sofa with a row of colourful shoes on the rug"></div>

  <article class="abs news-item" style="top:1000px">
    <span class="news-date">(5/17/2014)</span>
    <div class="news-body">
      <div class="news-title">Lorem ipsum dolor sit amet</div>
      <div class="news-text">Lorem ipsum dolor sit amet, consectetuer adipiscing elit. Aenean commodo ligula eget dolor. Aenean massa.</div>
    </div>
  </article>

  <article class="abs news-item" style="top:1056px">
    <span class="news-date">(5/16/2013)</span>
    <div class="news-body">
      <div class="news-title">Lorem ipsum dolor sit amet</div>
      <div class="news-text">Lorem ipsum dolor sit amet, consectetuer adipiscing elit. Aenean commodo ligula eget dolor. Aenean massa.</div>
    </div>
  </article>

  <svg class="abs more-arrow" viewBox="0 0 72 10"><path d="M2 2L36 8L70 2" fill="none" stroke="#666" stroke-width="1.5"/></svg>
</main>

<footer>
  <div class="abs footer-rule"></div>
  <nav class="abs footer-nav">
    <a class="active" style="left:226px">Home</a>
    <a style="left:283px">About Us</a>
    <a style="left:353px">Talvo Store</a>
    <a style="left:432px">Talvo Events</a>
    <a style="left:521px">News</a>
    <a style="left:573px">Contact</a>
  </nav>
  <p class="abs copyright">© 2014 Talvo shoes. All Rights Reserved.</p>
</footer>

</body>
</html>
```